Graphic Design for Free Community Event

We need a graphic created for a community event that is aimed at families with younger children called Totz Jam. This is a free event and has a fair/carnival feel to it with rides, games, and food. I need the graphic to be flexible enough to be able to be modified and used in a variety of ways on different print and digital marketing materials. I also need the centerpiece of the design to be an event logo that can be used as a standalone element.

The overall feel needs to be fun and friendly with a slightly modern edge to it. Attached are some images used in past events. These are for reference only and do not need to be simulated or used in the final product.

Target Market(s)

Families with children

Industry/Entity Type

Church

Font styles to use
Sans Serif

Requirements
Must have
• - Logo that incorporates the event name- Event Date: August 20 - Event Time: 10am - 2pm - Church name and logo incorporated: Bright Harbor Community Church (see attached logo files)
Nice to have
• - Bright colors- Flexible design elements that are interchangeable and scalable for use of the design in different layouts across different mediums and materials.
Should not have
• - Any references or images related to drugs, alcohol, tobacco, or other subjects that would be inappropriate for children.

```html
<!DOCTYPE html>
<html lang="en">
<head>
<meta charset="utf-8">
<title>Totz Jam – Free Community Event</title>
<link href="https://fonts.googleapis.com/css2?family=Lilita+One&family=Montserrat:wght@400;600;700&display=swap" rel="stylesheet">
<style>
  :root{
    --sun:#f7b20f;
    --orange:#f59a0e;
    --pink:#e23b62;
    --pink-deep:#c92a52;
    --teal:#1f9a86;
    --white:#ffffff;
    --paper:#fbfbf9;
    --stage:#efefec;
    --ink:#1d1d1f;
    --title-grey:#e4e4e4;
    --sky:#a9e3ef;
  }
  *{box-sizing:border-box;margin:0;padding:0}
  html,body{width:1200px;height:2282px;overflow:hidden}
  body{background:var(--stage);position:relative;font-family:"Montserrat",sans-serif}
  .poster{position:absolute;left:100px;top:431px;width:1000px;height:1420px;background:var(--paper);overflow:hidden;box-shadow:0 6px 18px rgba(0,0,0,.18)}
  .poster-backdrop{position:absolute;inset:0}
  .event-logo{position:absolute;left:0;width:100%;text-align:center;font-family:"Lilita One",sans-serif;text-transform:uppercase;line-height:.9}
  .event-logo .line-top{position:absolute;top:140px;left:0;width:100%;font-size:200px;color:var(--title-grey);text-shadow:0 10px 0 var(--pink-deep);letter-spacing:2px}
  .event-logo .line-bottom{position:absolute;top:318px;left:0;width:100%;font-size:200px;color:var(--sun);text-shadow:0 10px 0 var(--pink-deep);letter-spacing:6px}
  .kids-photo{position:absolute;left:60px;top:520px;width:880px;height:390px;border-radius:180px 180px 40px 40px;background:linear-gradient(180deg,#e9c26a 0%,#c8503e 45%,#3f5b8a 100%)}
  .info-bar{position:absolute;left:86px;top:935px;width:824px;height:113px;display:flex;border-radius:12px;overflow:hidden}
  .info-bar .cell{padding:14px 0 0 36px;color:var(--white)}
  .info-bar .date{background:var(--orange);width:420px;clip-path:polygon(0 0,100% 0,96% 100%,0 100%)}
  .info-bar .time{background:var(--pink);flex:1;margin-left:-18px;padding-left:44px}
  .info-bar .label{font-size:28px;font-weight:400;letter-spacing:1px}
  .info-bar .value{font-family:"Lilita One",sans-serif;font-size:50px;display:flex;align-items:center;gap:12px;line-height:1.1}
  .info-bar svg{width:34px;height:34px}
  .church-band{position:absolute;left:150px;top:1048px;width:715px;height:62px;background:var(--teal);clip-path:polygon(0 0,100% 0,94% 100%,6% 100%);color:var(--white);font-family:"Lilita One",sans-serif;font-size:36px;text-align:center;line-height:62px;text-transform:uppercase;letter-spacing:1px}
  .activities{position:absolute;left:94px;top:1130px;width:540px;height:170px}
  .activity{position:absolute;top:0;width:165px;height:155px;border:6px solid;border-radius:14px;overflow:hidden}
  .activity .thumb{position:absolute;inset:0}
  .activity .tag{position:absolute;left:0;right:0;bottom:0;height:44px;font-family:"Lilita One",sans-serif;font-size:28px;text-align:center;line-height:44px;text-transform:uppercase}
  .activity.rides{left:0;border-color:var(--pink);transform:rotate(-6deg)}
  .activity.rides .thumb{background:linear-gradient(160deg,#7fb3d6,#d94a4a)}
  .activity.rides .tag{background:var(--sun);color:var(--ink)}
  .activity.games{left:180px;top:8px;border-color:var(--teal);transform:rotate(7deg)}
  .activity.games .thumb{background:linear-gradient(180deg,#4f8a3a,#a6c46a)}
  .activity.games .tag{background:var(--teal);color:var(--white)}
  .activity.food{left:365px;border-color:var(--pink);transform:rotate(-10deg)}
  .activity.food .thumb{background:linear-gradient(150deg,#e8e2d6,#c9752f)}
  .activity.food .tag{background:var(--sun);color:var(--ink)}
  .free-event{position:absolute;left:670px;top:1145px;display:flex;align-items:flex-end;gap:8px}
  .free-event .lead{writing-mode:vertical-rl;transform:rotate(180deg);font-size:24px;color:var(--ink);letter-spacing:1px}
  .free-event .words{font-family:"Lilita One",sans-serif;font-size:72px;line-height:.85;text-transform:uppercase}
  .free-event .free{color:var(--pink)}
  .free-event .event{color:var(--sun)}
  .church-mark{position:absolute;left:90px;top:1316px;display:flex;align-items:center;gap:8px;width:285px}
  .church-mark .dot{flex:0 0 70px;width:70px;height:70px;border-radius:50%;background:var(--ink)}
  .church-mark .name{font-size:19px;font-weight:600;color:var(--ink);line-height:1.1;text-transform:uppercase;white-space:nowrap}
  .url-bar{position:absolute;left:388px;top:1321px;width:612px;height:62px;background:var(--sun);border-radius:31px 0 0 31px;display:flex;align-items:center;padding-left:24px;gap:14px;font-size:25px;color:var(--white);letter-spacing:2px;white-space:nowrap}
  .url-bar b{font-weight:700;color:var(--ink)}
  .url-bar svg{flex:0 0 30px;width:30px;height:30px}
</style>
</head>
<body>
<main class="poster">
  <svg class="poster-backdrop" viewBox="0 0 1000 1420" aria-hidden="true">
    <rect width="1000" height="650" fill="var(--sun)"/>
    <path d="M0 120 C80 60 120 200 60 300 C20 380 90 460 0 520 Z" fill="var(--orange)"/>
    <path d="M1000 200 C920 260 960 360 1000 420 Z" fill="var(--orange)"/>
    <path d="M0 480 C90 460 140 540 230 510 C330 480 360 560 500 540 C640 520 680 470 780 500 C880 530 930 450 1000 460 L1000 1420 L0 1420 Z" fill="var(--paper)"/>
    <circle cx="488" cy="423" r="391" fill="var(--pink)"/>
    <circle cx="488" cy="423" r="350" fill="none" stroke="var(--sun)" stroke-width="3" stroke-dasharray="12 10"/>
    <path d="M0 620 C60 560 140 560 190 610 C240 560 300 570 320 640 L320 700 L0 700 Z" fill="var(--white)"/>
    <path d="M1000 560 C940 520 870 540 850 600 C800 590 760 630 770 690 L1000 700 Z" fill="var(--white)"/>
    <ellipse cx="310" cy="80" rx="60" ry="22" fill="var(--sky)"/>
    <circle cx="40" cy="80" r="5" fill="var(--pink)"/>
    <circle cx="160" cy="88" r="5" fill="var(--pink)"/>
    <circle cx="970" cy="470" r="6" fill="#4a4aa8"/>
    <circle cx="900" cy="140" r="5" fill="var(--white)"/>
  </svg>

  <h1 class="event-logo" aria-label="Totz Jam">
    <span class="line-top">Totz</span>
    <span class="line-bottom">Jam</span>
  </h1>

  <div class="kids-photo" role="img" aria-label="Photo of five smiling children sitting together cross-legged"></div>

  <section class="info-bar">
    <div class="cell date">
      <p class="label">EVENT DATE</p>
      <p class="value">
        <svg viewBox="0 0 24 24" fill="none" stroke="currentColor" stroke-width="2"><rect x="3" y="5" width="18" height="16" rx="2"/><path d="M3 10h18M8 3v4M16 3v4"/></svg>
        AUGUST 20
      </p>
    </div>
    <div class="cell time">
      <p class="label">EVENT TIME</p>
      <p class="value">
        <svg viewBox="0 0 24 24" fill="none" stroke="currentColor" stroke-width="2"><circle cx="12" cy="12" r="9"/><path d="M12 7v5l3 2"/></svg>
        10AM - 2PM
      </p>
    </div>
  </section>
  <div class="church-band">Bright Harbor Community Church</div>

  <section class="activities">
    <figure class="activity rides"><div class="thumb" role="img" aria-label="Children on a fairground ride"></div><figcaption class="tag">Rides</figcaption></figure>
    <figure class="activity games"><div class="thumb" role="img" aria-label="Children playing games on grass"></div><figcaption class="tag">Games</figcaption></figure>
    <figure class="activity food"><div class="thumb" role="img" aria-label="Table of festival food dishes"></div><figcaption class="tag">Food</figcaption></figure>
  </section>

  <div class="free-event">
    <span class="lead">THIS IS A</span>
    <p class="words"><span class="free">FREE</span><br><span class="event">EVENT</span></p>
  </div>

  <footer>
    <div class="church-mark"><span class="dot"></span><p class="name">Bright Harbor<br>Community Church</p></div>
    <div class="url-bar">
      <svg viewBox="0 0 24 24" fill="none" stroke="var(--ink)" stroke-width="2"><circle cx="12" cy="12" r="9"/><path d="M3 12h18M12 3c3 3 3 15 0 18M12 3c-3 3-3 15 0 18"/></svg>
      <span>www.<b>brightharborchurch</b>.com</span>
    </div>
  </footer>
</main>
</body>
</html>
```